Business Card Design

A new interior design company specialising in residential property styling, with a focus on styling properties for sale. We aim to present the property to increase marketability, saleability and hopefully get the best price.
We are looking for a design that stands out from the crowd maybe using colour and maybe pattern, something that is modern and fits in with companies aesthetic of design.
We would like the design not to be too fussy, with perhaps all of the contact information on the back (ie just the company name on front?)

Industry/Entity Type

Residential

Contact Information for Business Card

Brisa Interiors, Tessa Wingrove, Interior Designer,0417365209, brisainteriors@quolmail.com.au

Requirements
Nice to have
• Brisa means "love" in Spanish and I was wondering whether it might be too corny to use the M in bRisa that resembles a love heart, something curvy. This is just an idea I've was toying with and I am completely open to other suggestions.

```html
<!DOCTYPE html>
<html lang="en">
<head>
<meta charset="utf-8">
<title>Brisa Interiors – Business Card</title>
<link rel="stylesheet" href="https://fonts.googleapis.com/css2?family=Mulish:wght@300;400;700&display=swap">
<style>
  :root {
    --page-bg: #ffffff;
    --front-bg: #272727;
    --brand-text: #f2f2f2;
    --back-light: #ef5b45;
    --back-mid: #d2463a;
    --back-dark: #b22c27;
    --text-light: #ffffff;
    --card-shadow: rgba(0, 0, 0, 0.35);
  }
  * { margin: 0; padding: 0; box-sizing: border-box; }
  html, body {
    width: 1200px;
    height: 1000px;
    overflow: hidden;
    background: var(--page-bg);
    font-family: "Mulish", "Century Gothic", sans-serif;
  }
  .sheet {
    position: relative;
    width: 1200px;
    height: 1000px;
  }
  .card {
    position: absolute;
    top: 122px;
    width: 438px;
    height: 758px;
    box-shadow: 3px 4px 6px var(--card-shadow);
  }
  .card-front {
    left: 143px;
    background: var(--front-bg);
  }
  .card-back {
    left: 612px;
    background: radial-gradient(circle at 34% 18%, var(--back-light) 0%, var(--back-mid) 45%, var(--back-dark) 85%);
    color: var(--text-light);
  }
  .brand {
    position: absolute;
    left: 0;
    right: 0;
    top: 350px;
    text-align: center;
    color: var(--brand-text);
    font-size: 46px;
    font-weight: 700;
    line-height: 1.1;
  }
  .contact-block {
    position: absolute;
    left: 0;
    right: 0;
    top: 332px;
    text-align: center;
  }
  .person-name {
    font-size: 22px;
    font-weight: 700;
    line-height: 26px;
  }
  .person-role {
    font-size: 16px;
    font-weight: 400;
    line-height: 20px;
  }
  .contact-list {
    list-style: none;
    margin-top: 30px;
    font-size: 19px;
    font-weight: 300;
    line-height: 25px;
  }
  .contact-item {
    display: flex;
    align-items: center;
    justify-content: center;
    gap: 10px;
  }
  .contact-icon {
    width: 24px;
    height: 18px;
    fill: var(--text-light);
  }
</style>
</head>
<body>
<main class="sheet">
  <section class="card card-front" aria-label="Card front">
    <h1 class="brand">Brisa Interiors</h1>
  </section>

  <section class="card card-back" aria-label="Card back">
    <div class="contact-block">
      <p class="person-name">Tessa Wingrove</p>
      <p class="person-role">Interior Designer</p>
      <ul class="contact-list">
        <li class="contact-item">
          <svg class="contact-icon" viewBox="0 0 24 18" aria-hidden="true">
            <path d="M1 6 C1 2 23 2 23 6 L23 8 L17 8 L17 5.5 C14 4.5 10 4.5 7 5.5 L7 8 L1 8 Z"/>
            <path d="M6 9 L18 9 L21 17 L3 17 Z"/>
            <circle cx="12" cy="12.5" r="2.4" fill="#c9392f"/>
          </svg>
          <span>0417365209</span>
        </li>
        <li class="contact-item">
          <svg class="contact-icon" viewBox="0 0 24 18" aria-hidden="true">
            <path d="M1 2 L23 2 L23 16 L1 16 Z"/>
            <path d="M2 3 L12 10.5 L22 3" fill="none" stroke="#c9392f" stroke-width="1.6"/>
            <path d="M2 15 L9.5 8.5 M22 15 L14.5 8.5" fill="none" stroke="#c9392f" stroke-width="1.2"/>
          </svg>
          <span>brisainteriors@quolmail.com.au</span>
        </li>
      </ul>
    </div>
  </section>
</main>
</body>
</html>
```